We have a blog www.lottamarie.eu based on WordPress (Wix would be also good) about homeopathy-critique and health issues.
Our logo is a little girl Hildegard, the background color green.
It looks somehow good, but we want to be up to date:).
Our goal is to open eyes from propaganda and misinformation on the web. We are all volunteers and invest our time and money for this purpose. Once people like it, we are happy to translate our blog to the English.
Updates

Please, don't submit a new design. we will choose from the designs we already have. Thank you! Added Thursday, July 20, 2017

Target Market(s)

mothers, people reading about health

Industry/Entity Type

Health

Number of Pages Required

3 page

Colors
abd037

Requirements
Must have
• - nice, friendly, evoking positive emotions
• - colorful (see for example how it looks now)
• - a good way how to show up articles (actually, if you open an article, you have to scroll, it appears on the bottom of the page)
• - We need to arrange stuff, where to put "most read", "Category", "contact", "themes" "search" (now, everything is on the right side. if you like it so, ok)
Nice to have
• Everything is in German, but I am happy to translate everything you need.
• The big text is: Lottchen mag kein Kraut: Hildegard wants no Kraut (the sugar pills of homeopathy)
• "(Nicht nur) homöopathiekritische Informationen für Eltern und alle, die für unsere Kleinen sorgen" - (Not only) Homeopathy-critique Information for Parents and All Who Take Care Of Our Small (Children)
• - there are many of the pictures of Hildegard, you can choose the best one. You can find them here https://www.verbund-klartext.eu/lottchen-mag-kein-kraut
• - we have also a FB, which could be integrated https://www.facebook.com/lottchenmagkeinkraut/?fref=ts
Should not have
• - a sterile modern look

```html
<!DOCTYPE html>
<html lang="de">
<head>
<meta charset="utf-8">
<title>Lottchen mag kein Kraut – Blog</title>
<link rel="stylesheet" href="https://fonts.googleapis.com/css2?family=Montserrat:wght@400;500;600;700&family=Open+Sans:ital,wght@0,400;0,600;1,400&display=swap">
<style>
:root{
  --green:#abd037;
  --green-text:#9bc43a;
  --blue:#3a4f9b;
  --red:#e8262b;
  --ink:#222;
  --grey:#8a8a8a;
  --line:#e6e6e6;
  --page:#f4f4f4;
  --white:#fff;
  --dark:#231f20;
  --fold:#d9d9d9;
}
*{box-sizing:border-box;margin:0;padding:0}
html,body{width:1200px;height:2359px;overflow:hidden}
body{position:relative;background:var(--white);font-family:"Open Sans",Arial,sans-serif;color:var(--ink)}

/* header */
.site-header{position:absolute;left:0;top:0;width:1200px;height:82px;background:var(--white)}
.brand{position:absolute;display:flex;align-items:center;gap:6px}
.brand-dot{width:26px;height:26px;border-radius:50%;background:var(--green);flex:none}
.brand-name{font-family:"Montserrat",sans-serif;font-weight:700;font-size:11px;line-height:12px;color:var(--blue);width:70px}
.site-header .brand{left:268px;top:18px}
.account{position:absolute;left:686px;top:18px;font-size:10.5px;color:#555;display:flex;align-items:center;gap:5px}
.account .sep{color:#bbb;margin:0 3px}
.social-top{position:absolute;left:814px;top:21px;display:flex;gap:13px}
.social-top span{width:9px;height:9px;border-radius:50%;background:#333}
.social-top span.on{background:var(--green)}
.main-nav{position:absolute;top:46px;left:463px;display:flex;font-family:"Montserrat",sans-serif;font-size:11px;color:#333}
.main-nav a{text-decoration:none;color:inherit;margin-right:33px}
.main-nav a.active{color:var(--green-text)}
.search-icon{position:absolute;left:922px;top:48px}

/* hero */
.hero{position:absolute;left:0;top:82px;width:1200px;height:308px;overflow:hidden}
.hero-side{position:absolute;top:0;height:308px}
.hero-side.left{left:0;width:248px;background:linear-gradient(160deg,#eef0ee 0%,#f3ece0 45%,#e5e9e3 100%)}
.hero-side.right{left:950px;width:250px;background:radial-gradient(ellipse at 60% 55%,#f5ecd7 0%,#dfe9f3 55%,#eef2f6 100%)}
.hero-side .slide-text{position:absolute;font-size:21px;color:#9a9a9a;white-space:nowrap}
.hero-center{position:absolute;left:248px;top:0;width:702px;height:308px;background:linear-gradient(135deg,#6d6a58 0%,#5d5a4c 50%,#6a6453 100%)}
.hero-shade{position:absolute;inset:0;background:rgba(45,42,38,.55)}
.hero-title{position:absolute;left:0;width:702px;top:86px;text-align:center;font-family:"Montserrat",sans-serif;font-weight:400;font-size:21px;line-height:28px;color:var(--white);letter-spacing:.3px}
.hero-btn{position:absolute;left:304px;top:190px;width:94px;height:24px;border:1px solid var(--white);color:var(--white);font-family:"Montserrat",sans-serif;font-size:9.5px;line-height:22px;text-align:center}
.hero-dots{position:absolute;left:334px;top:283px;display:flex;gap:4px}
.hero-dots span{width:4px;height:4px;border-radius:50%;background:#ddd}
.hero-dots span.on{background:var(--white);width:6px;height:6px;margin-top:-1px}
.hero-arrow{position:absolute;top:115px;width:24px;height:78px;border:1px solid #555;background:rgba(255,255,255,.5);font-family:"Montserrat",sans-serif;font-size:8px;color:#333;display:flex;flex-direction:column;align-items:center;justify-content:center;line-height:11px}
.hero-arrow.prev{left:201px}
.hero-arrow.next{left:973px;border-color:#ccc;color:#fff;background:transparent}

/* content */
.content{position:absolute;left:0;top:390px;width:1200px;height:1576px;background:var(--page)}
.section-title{position:absolute;top:432px;left:0;width:1200px;text-align:center;font-family:"Montserrat",sans-serif;font-weight:600;font-size:21px;color:var(--ink)}

.card{position:absolute;background:var(--white);box-shadow:0 1px 2px rgba(0,0,0,.05)}
.card::after,.widget::after{content:"";position:absolute;right:0;bottom:0;border-style:solid;border-width:0 0 14px 14px;border-color:transparent transparent var(--page) var(--fold)}
.card .thumb{position:absolute;left:11px;top:11px;right:11px}
.card .tag{position:absolute;left:50%;transform:translateX(-50%);background:var(--red);color:var(--white);font-family:"Montserrat",sans-serif;font-weight:700;font-size:8px;letter-spacing:.6px;padding:0 10px;height:17px;line-height:17px}
.card .body{position:absolute;left:0;right:0;text-align:center}
.card .title{margin:0 8px;font-family:"Montserrat",sans-serif;font-weight:600;font-size:13px;line-height:18.5px;color:var(--ink)}
.card .date{margin-top:4px;font-size:8.5px;line-height:12px;font-style:italic;color:#aaa}
.card .excerpt{margin:10px 16px 0;font-size:9px;line-height:14.5px;color:var(--grey)}
.card .meta{position:absolute;left:16px;right:16px;height:25px;border-top:1px solid var(--line);border-bottom:1px solid var(--line);display:flex;justify-content:space-between;align-items:center;font-size:8.5px;color:#777;padding:0 4px}
.card .meta span{display:flex;align-items:center;gap:4px}
.card .more{position:absolute;left:0;right:0;text-align:center;font-size:9px;color:var(--green-text)}

.card.feature{left:267px;top:492px;width:436px;height:444px}
.card.feature .thumb{height:186px}
.card.feature .tag{top:188px}
.card.feature .body{top:226px}
.card.feature .title{font-size:14.5px}
.card.feature .excerpt{margin:12px 30px 0}
.card.feature .meta{top:356px;padding:0 14px}
.card.feature .more{top:408px}

.card.small{width:208px;height:443px}
.card.small .thumb{height:143px}
.card.small .tag{top:145px}
.card.small .body{top:182px}
.card.small .meta{top:347px}
.card.small .more{top:398px}

.pager{position:absolute;top:1898px;left:321px;display:flex;align-items:center;font-family:"Montserrat",sans-serif;font-size:9px;color:#555}
.pager .step{width:71px;height:21px;background:var(--white);text-align:center;line-height:21px;font-size:7.5px;letter-spacing:.8px;font-weight:600}
.pager .pages{display:flex;gap:8px;margin:0 25px}
.pager .pages span{width:22px;height:22px;line-height:22px;text-align:center}
.pager .pages span.on{background:var(--green);color:var(--white)}

/* sidebar */
.widget{position:absolute;left:722px;width:209px;background:var(--white)}
.widget-head{height:35px;background:var(--blue);color:var(--white);font-family:"Montserrat",sans-serif;font-weight:600;font-size:14px;text-align:center;line-height:35px}
.widget.about{top:495px;height:323px}
.avatar{position:absolute;left:65px;top:55px;width:80px;height:112px;border-radius:50% 50% 45% 45%;background:radial-gradient(circle at 50% 45%,#fde7c2 0%,#f8d13c 60%,#f2c318 100%)}
.about-text{position:absolute;left:14px;right:14px;top:183px;text-align:center;font-size:8.5px;line-height:13px;color:var(--grey)}
.btn-green{position:absolute;left:57px;top:261px;width:96px;height:24px;background:var(--green);color:var(--white);font-family:"Montserrat",sans-serif;font-size:9px;text-align:center;line-height:24px}
.widget.categories{top:835px;height:376px}
.cat-list{list-style:none;position:absolute;left:12px;right:12px;top:48px}
.cat-list li{height:30.8px;line-height:30px;border-bottom:1px solid var(--line);font-size:8.8px;color:#777}
.widget.popular{top:1233px;height:359px}
.pop-item{position:absolute;left:12px;right:12px;height:66px;border-bottom:1px solid var(--line)}
.pop-item .pic{position:absolute;left:0;top:6px;width:55px;height:55px}
.pop-item .pop-title{position:absolute;left:66px;top:6px;font-family:"Montserrat",sans-serif;font-weight:600;font-size:9px;line-height:12px;color:var(--ink)}
.pop-item .pop-date{font-family:"Open Sans",sans-serif;font-weight:400;font-size:7.5px;color:var(--red);display:block;margin-top:1px}
.btn-outline{position:absolute;left:57px;top:296px;width:96px;height:24px;border:1px solid #555;font-family:"Montserrat",sans-serif;font-size:9px;text-align:center;line-height:22px;color:#333}
.widget.social{top:1610px;height:254px}
.social-feed{position:absolute;left:12px;top:57px;width:185px;height:110px;background:linear-gradient(180deg,#e8eaef 0%,#f2f2f2 55%,#eceff3 100%);border:1px solid #dcdcdc}

/* footer */
.footer-top{position:absolute;left:0;top:1966px;width:1200px;height:239px;background:var(--white)}
.footer-top .brand{left:562px;top:42px;flex-direction:column;gap:4px}
.footer-top .brand-name{text-align:center}
.footer-blurb{position:absolute;top:134px;left:0;width:1200px;text-align:center;font-size:9.5px;line-height:16px;color:var(--grey)}
.footer-sub{position:absolute;top:186px;left:0;width:1200px;text-align:center;font-family:"Montserrat",sans-serif;font-weight:600;font-size:13.5px}
.footer-bottom{position:absolute;left:0;top:2205px;width:1200px;height:154px;background:var(--dark)}
.subscribe{position:absolute;z-index:2;left:466px;top:2192px;width:268px;height:24px;display:flex;border:1px solid #e2e2e2;background:var(--white)}
.subscribe .field{flex:1;font-size:8.5px;color:#999;line-height:22px;padding-left:10px}
.subscribe .send{width:23px;background:var(--red);display:flex;align-items:center;justify-content:center}
.footer-social{position:absolute;left:507px;top:37px;display:flex;gap:8px}
.footer-social span{width:24px;height:24px;border-radius:50%;border:1px solid #ccc}
.footer-social span.on{border-color:var(--green);background:rgba(171,208,55,.15)}
.copyright{position:absolute;top:96px;left:0;width:1200px;text-align:center;font-size:8.5px;color:#bbb}
</style>
</head>
<body>

<header class="site-header">
  <div class="brand"><span class="brand-dot"></span><span class="brand-name">Lottchen mag kein Kraut</span></div>
  <div class="account">
    <svg width="9" height="10" viewBox="0 0 9 10"><circle cx="4.5" cy="3" r="2.2" fill="none" stroke="#666"/><path d="M1 9.5c0-2.2 1.6-3.5 3.5-3.5S8 7.3 8 9.5" fill="none" stroke="#666"/></svg>
    <span>Login</span><span class="sep">/</span><span>Sign Up</span>
  </div>
  <div class="social-top" aria-label="Soziale Netzwerke">
    <span></span><span class="on"></span><span></span><span></span><span></span><span></span>
  </div>
  <nav class="main-nav">
    <a class="active" href="#">Home / Beitragsseite</a>
    <a href="#">Willkommen beim Lottchen!</a>
    <a href="#">Lottchens Shop</a>
  </nav>
  <svg class="search-icon" width="11" height="11" viewBox="0 0 11 11"><circle cx="4.5" cy="4.5" r="3.4" fill="none" stroke="#222" stroke-width="1.6"/><path d="M7 7l3.2 3.2" stroke="#222" stroke-width="1.8"/></svg>
</header>

<section class="hero">
  <div class="hero-side left" role="img" aria-label="Illustration: Hildegard baut eine Sandburg unter einem Sonnenschirm">
    <span class="slide-text" style="left:18px;top:14px">Sommer, Sonne, Sonn</span>
    <span class="slide-text" style="left:0;top:276px;font-size:20px">Globuli sind weder Schu</span>
  </div>
  <div class="hero-side right" role="img" aria-label="Illustration: Hildegard mit Sonnenhut im Schlauchboot">
    <span class="slide-text" style="left:176px;top:280px;font-size:15px">www.ver</span>
  </div>
  <div class="hero-center" role="img" aria-label="Illustration: Hildegard mit Freundin in einem Zimmer">
    <div class="hero-shade"></div>
    <h1 class="hero-title">(Not only) Homeopathy-critique<br>Information for Parents and All Who<br>Take Care Of Our Small (Children)</h1>
    <div class="hero-btn">Read More</div>
    <div class="hero-dots"><span></span><span></span><span class="on"></span><span></span></div>
  </div>
  <div class="hero-arrow prev"><span>P</span><span>R</span><span>E</span><span>V</span></div>
  <div class="hero-arrow next"><span>N</span><span>E</span><span>X</span><span>T</span></div>
</section>

<main class="content"></main>
<h2 class="section-title">Our Latest Blog</h2>

<article class="card feature">
  <div class="thumb" role="img" aria-label="Foto: Jack-Russell-Terrier mit roter Leine" style="background:linear-gradient(100deg,#b9a58e 0%,#d8cfc2 40%,#9f8a72 75%,#c6b8a6 100%)"></div>
  <span class="tag">ANIMALS</span>
  <div class="body">
    <h3 class="title">Tierhomöopathie ??? ...</h3>
    <p class="date">Published On July 16, 2017</p>
    <p class="excerpt">The vast majority of you are certainly animal friends, especially our little ones. For many, therefore, there is also an animal companion in the family, whom the children in particular do not want to miss. This is the reason why the Lottchen, because of her own friend Bello, considers it important to publish...</p>
  </div>
  <div class="meta">
    <span><svg width="9" height="9" viewBox="0 0 9 9"><circle cx="4.5" cy="2.6" r="2" fill="none" stroke="#888"/><path d="M1 8.8c0-2 1.5-3.3 3.5-3.3S8 6.8 8 8.8" fill="none" stroke="#888"/></svg>Lorem</span>
    <span><svg width="10" height="9" viewBox="0 0 10 9"><path d="M1 1h8v5H4L2 8V6H1z" fill="none" stroke="#888"/></svg>30 Comment</span>
    <span><svg width="10" height="9" viewBox="0 0 10 9"><path d="M5 8.3L1.3 4.6A2 2 0 0 1 5 2a2 2 0 0 1 3.7 2.6z" fill="none" stroke="#888"/></svg>25 Likes</span>
    <span><svg width="9" height="9" viewBox="0 0 9 9"><circle cx="7" cy="1.8" r="1.4" fill="#555"/><circle cx="2" cy="4.5" r="1.4" fill="#555"/><circle cx="7" cy="7.2" r="1.4" fill="#555"/><path d="M7 1.8L2 4.5 7 7.2" stroke="#555" fill="none"/></svg>Share</span>
  </div>
  <p class="more">Continue Reading</p>
</article>

<article class="card small" style="left:267px;top:956px">
  <div class="thumb" role="img" aria-label="Foto: Regal mit Gläsern voller Globuli" style="background:linear-gradient(180deg,#7a5a3c 0%,#a5794e 45%,#c9b48f 70%,#8a6d4f 100%)"></div>
  <span class="tag">PLACEBO</span>
  <div class="body">
    <h3 class="title">Selbstmedikation mit Homöopathie – klar! ... oder doch nicht so klar?</h3>
    <p class="date">Published On July 16, 2017</p>
    <p class="excerpt">The vast majority of you are certainly animal friends, especially our little ones. For many, therefore, there is also an animal companion whom...</p>
  </div>
  <div class="meta">
    <span><svg width="9" height="9" viewBox="0 0 9 9"><circle cx="4.5" cy="2.6" r="2" fill="none" stroke="#888"/><path d="M1 8.8c0-2 1.5-3.3 3.5-3.3S8 6.8 8 8.8" fill="none" stroke="#888"/></svg>Lorem</span>
    <span><svg width="10" height="9" viewBox="0 0 10 9"><path d="M1 1h8v5H4L2 8V6H1z" fill="none" stroke="#888"/></svg>30 Comment</span>
    <span><svg width="9" height="9" viewBox="0 0 9 9"><circle cx="7" cy="1.8" r="1.4" fill="#555"/><circle cx="2" cy="4.5" r="1.4" fill="#555"/><circle cx="7" cy="7.2" r="1.4" fill="#555"/><path d="M7 1.8L2 4.5 7 7.2" stroke="#555" fill="none"/></svg>Share</span>
  </div>
  <p class="more">Continue Reading</p>
</article>

<article class="card small" style="left:497px;top:956px">
  <div class="thumb" role="img" aria-label="Schwarzweiß-Porträtfoto eines Mannes" style="background:linear-gradient(90deg,#d8d8d8 0%,#6e6e6e 40%,#3c3c3c 60%,#bdbdbd 100%)"></div>
  <span class="tag">ALLGEMEIN</span>
  <div class="body">
    <h3 class="title">Ein paar Gedanken zur anthroposophischen Medizin</h3>
    <p class="date">Published On July 16, 2017</p>
    <p class="excerpt">Nicht so populär wie Homöopathie – Anthroposophische Medizin, ein Teil des anthroposophischen Universums. Aber nicht zu vernachlässigen...</p>
  </div>
  <div class="meta">
    <span><svg width="9" height="9" viewBox="0 0 9 9"><circle cx="4.5" cy="2.6" r="2" fill="none" stroke="#888"/><path d="M1 8.8c0-2 1.5-3.3 3.5-3.3S8 6.8 8 8.8" fill="none" stroke="#888"/></svg>Lorem</span>
    <span><svg width="10" height="9" viewBox="0 0 10 9"><path d="M1 1h8v5H4L2 8V6H1z" fill="none" stroke="#888"/></svg>30 Comment</span>
    <span><svg width="9" height="9" viewBox="0 0 9 9"><circle cx="7" cy="1.8" r="1.4" fill="#555"/><circle cx="2" cy="4.5" r="1.4" fill="#555"/><circle cx="7" cy="7.2" r="1.4" fill="#555"/><path d="M7 1.8L2 4.5 7 7.2" stroke="#555" fill="none"/></svg>Share</span>
  </div>
  <p class="more">Continue Reading</p>
</article>

<article class="card small" style="left:267px;top:1423px">
  <div class="thumb" role="img" aria-label="Foto: zwei Fläschchen über grünem Hintergrund mit Globuli" style="background:linear-gradient(180deg,#a6d93a 0%,#93cd2a 60%,#b5df55 100%)"></div>
  <span class="tag">PLACEBO</span>
  <div class="body">
    <h3 class="title">Thema: Placebo – Heute: Was sind Placebo und Placeboeffekt?</h3>
    <p class="date">Published On July 16, 2017</p>
    <p class="excerpt">Klären wir zunächst einmal, was man unter dem Begriff „Placebo“ im Zusammenhang mit Arznei versteht. Bei einem Placebo handelt es...</p>
  </div>
  <div class="meta">
    <span><svg width="9" height="9" viewBox="0 0 9 9"><circle cx="4.5" cy="2.6" r="2" fill="none" stroke="#888"/><path d="M1 8.8c0-2 1.5-3.3 3.5-3.3S8 6.8 8 8.8" fill="none" stroke="#888"/></svg>Lorem</span>
    <span><svg width="10" height="9" viewBox="0 0 10 9"><path d="M1 1h8v5H4L2 8V6H1z" fill="none" stroke="#888"/></svg>30 Comment</span>
    <span><svg width="9" height="9" viewBox="0 0 9 9"><circle cx="7" cy="1.8" r="1.4" fill="#555"/><circle cx="2" cy="4.5" r="1.4" fill="#555"/><circle cx="7" cy="7.2" r="1.4" fill="#555"/><path d="M7 1.8L2 4.5 7 7.2" stroke="#555" fill="none"/></svg>Share</span>
  </div>
  <p class="more">Continue Reading</p>
</article>

<article class="card small" style="left:497px;top:1423px">
  <div class="thumb" role="img" aria-label="Foto: schlafendes Baby in rosa Decke" style="background:linear-gradient(160deg,#c9a9c0 0%,#e9cfc4 45%,#d9b0c6 100%)"></div>
  <span class="tag">HAUSMITTEL</span>
  <div class="body">
    <h3 class="title">Apis mellifica – Was tut die Biene in den Globuli?</h3>
    <p class="date">Published On July 3, 2017</p>
    <p class="excerpt">Natürlich nichts mehr, sie ist ja tot, und außerdem ist höchstwahrscheinlich gar nichts von ihr drin. Eines der homöopathischen Mittel...</p>
  </div>
  <div class="meta">
    <span><svg width="9" height="9" viewBox="0 0 9 9"><circle cx="4.5" cy="2.6" r="2" fill="none" stroke="#888"/><path d="M1 8.8c0-2 1.5-3.3 3.5-3.3S8 6.8 8 8.8" fill="none" stroke="#888"/></svg>Lorem</span>
    <span><svg width="10" height="9" viewBox="0 0 10 9"><path d="M1 1h8v5H4L2 8V6H1z" fill="none" stroke="#888"/></svg>30 Comment</span>
    <span><svg width="9" height="9" viewBox="0 0 9 9"><circle cx="7" cy="1.8" r="1.4" fill="#555"/><circle cx="2" cy="4.5" r="1.4" fill="#555"/><circle cx="7" cy="7.2" r="1.4" fill="#555"/><path d="M7 1.8L2 4.5 7 7.2" stroke="#555" fill="none"/></svg>Share</span>
  </div>
  <p class="more">Continue Reading</p>
</article>

<nav class="pager">
  <span class="step">PREV</span>
  <div class="pages"><span class="on">1</span><span>2</span><span>3</span><span>4</span><span>5</span></div>
  <span class="step">NEXT</span>
</nav>

<aside>
  <section class="widget about">
    <h4 class="widget-head">About Us</h4>
    <div class="avatar" role="img" aria-label="Illustration: Maskottchen Hildegard mit blonden Locken"></div>
    <p class="about-text">Ganz herzlich willkommen auf der Webseite von Lottchen und ihren Freundinnen, den Maskottchen des Informationsverbunds Klartext!...</p>
    <div class="btn-green">Read More</div>
  </section>

  <section class="widget categories">
    <h4 class="widget-head">Categories</h4>
    <ul class="cat-list">
      <li>Anthroposophy</li><li>Hausmittel</li><li>Globuli</li><li>Good Medicine</li><li>Medical</li>
      <li>Practitioner</li><li>Homeopathy</li><li>Pediatrician</li><li>Medicine</li><li>Animal Health</li>
    </ul>
  </section>

  <section class="widget popular">
    <h4 class="widget-head">Most Read</h4>
    <div class="pop-item" style="top:52px">
      <div class="pic" role="img" aria-label="Foto: Hund" style="background:linear-gradient(120deg,#c6a784,#8c6a4c)"></div>
      <p class="pop-title">Tierhomöopathie ???<span class="pop-date">Published On July 16, 2017</span></p>
    </div>
    <div class="pop-item" style="top:128px">
      <div class="pic" role="img" aria-label="Foto: Menschen an einem Konferenztisch" style="background:linear-gradient(120deg,#d9d4c8,#9a9388)"></div>
      <p class="pop-title">Topic: Placebo -<br>Today: Placebo is not<br>imagination!<span class="pop-date">Published On July 16, 2017</span></p>
    </div>
    <div class="pop-item" style="top:203px">
      <div class="pic" role="img" aria-label="Foto: Gruppe von Personen" style="background:linear-gradient(120deg,#cfd0cc,#8c8c86)"></div>
      <p class="pop-title">“Idols” as health “ad-<br>visors”?<span class="pop-date">Published On July 16, 2017</span></p>
    </div>
    <div class="btn-outline">Explore More</div>
  </section>

  <section class="widget social">
    <h4 class="widget-head">Freundebuch</h4>
    <div class="social-feed" role="img" aria-label="Eingebettete Seitenvorschau von Lottchen mag kein Kraut"></div>
  </section>
</aside>

<footer>
  <div class="footer-top">
    <div class="brand"><span class="brand-dot"></span><span class="brand-name">Lottchen mag kein Kraut</span></div>
    <p class="footer-blurb">There are many variations of passages of Lorem Ipsum available,<br>majority have suffered alteration in some form, by injected humour, or ran-</p>
    <h5 class="footer-sub">Email Subscription</h5>
  </div>
  <div class="footer-bottom">
    <div class="footer-social" aria-label="Soziale Netzwerke">
      <span></span><span class="on"></span><span></span><span></span><span></span><span></span>
    </div>
    <p class="copyright">Copyright © 2016 Lottchen. All Rights Reserved</p>
  </div>
  <div class="subscribe">
    <span class="field">Enter Your Email...</span>
    <span class="send"><svg width="10" height="10" viewBox="0 0 10 10"><path d="M1 5L9 1 7 9 5 6z" fill="#fff"/></svg></span>
  </div>
</footer>

</body>
</html>
```